New Business Card for our Indoor Golf Training Facility

We are looking for designs for a new business card for our indoor golf training facility. Attached is our logo, our logo with our slogan, and here is our elevator pitch (What makes us different from the others) not sure if all the info will fit on one card, maybe you can condense the elevator pitch? here is the info

Elevator Pitch
We work with serious golfers and those that want to be serious golfers…
to make you better, faster, at all phases of the game…
We use the same state-of-the-art technology as professional golfers…
which produces data sets that shows your improvement in real time.
Our facility is available 24/7 to our members, which allows you to improve on your time.

our website: www.brambleteegolf.com

Target Market(s)

Golfers

Font styles to use
Serif
Sans Serif

Colors
ec1f27
f59195
fbd4d5
919191
d3d3d3
1b1b1b

Requirements
Must have
• our logo or our logo with the slogan, elevator pitch (can be condensed or shortened)

```html
<!DOCTYPE html>
<html lang="en">
<head>
<meta charset="utf-8">
<title>Bramble Tee Golf – Business Card</title>
<link rel="stylesheet" href="https://fonts.googleapis.com/css2?family=Oswald:wght@500&family=Work+Sans:wght@400;600;700&display=swap">
<style>
  :root {
    --backdrop: #2b2b2b;
    --card: #1b1b1b;
    --card-edge: #141414;
    --ink-light: #d3d3d3;
    --ink-mid: #919191;
    --ink-dark: #0c0c0c;
    --ink-deep: #111111;
  }
  * { margin: 0; padding: 0; box-sizing: border-box; }
  html, body { width: 1200px; height: 900px; overflow: hidden; }
  body {
    background: var(--backdrop);
    font-family: "Work Sans", sans-serif;
    display: flex;
    flex-direction: column;
    align-items: center;
    justify-content: center;
    gap: 40px;
  }
  .card {
    width: 660px;
    height: 377px;
    background: var(--card);
    border: 1px solid var(--card-edge);
    box-shadow: 0 10px 30px rgba(0,0,0,.45);
    position: relative;
  }

  /* Front */
  .card--front {
    display: flex;
    flex-direction: column;
    align-items: center;
    padding-top: 52px;
  }
  .brand { display: flex; align-items: center; gap: 14px; }
  .brand__dot {
    width: 44px; height: 44px; border-radius: 50%;
    border: 2px solid var(--ink-dark);
  }
  .brand__name {
    font-weight: 700; font-size: 42px; color: var(--ink-light);
    letter-spacing: .5px; line-height: 1;
  }
  .slogan {
    margin-top: 8px; font-size: 15px; color: var(--ink-mid); letter-spacing: .6px;
  }
  .pitch { margin-top: 34px; text-align: center; }
  .pitch__title { font-size: 15px; color: var(--ink-mid); margin-bottom: 8px; }
  .pitch__line { font-size: 12.5px; line-height: 1.55; color: var(--ink-deep); }
  .pitch__line--lit { color: var(--ink-mid); }

  /* Back */
  .card--back { padding: 0 56px; }
  .identity {
    position: absolute; top: 128px; left: 56px;
    display: flex; align-items: center;
  }
  .person { text-align: right; padding-right: 26px; }
  .person__name {
    font-family: "Oswald", sans-serif; font-weight: 500;
    font-size: 36px; letter-spacing: 1px; color: var(--ink-dark);
    text-shadow: 0 1px 0 rgba(255,255,255,.06); line-height: 1.1;
  }
  .person__role { font-size: 15px; color: var(--ink-mid); letter-spacing: .5px; }
  .divider { width: 1px; height: 62px; background: var(--ink-mid); }
  .contacts { list-style: none; padding-left: 26px; }
  .contacts li {
    display: flex; align-items: center; gap: 12px;
    font-size: 17px; color: var(--ink-light); letter-spacing: .6px; line-height: 1.55;
  }
  .contacts svg { width: 12px; height: 12px; flex: none; }
  .address {
    position: absolute; left: 56px; bottom: 52px;
    font-size: 17px; letter-spacing: .6px; color: var(--ink-mid);
  }
  .address__dim { color: var(--ink-dark); }
</style>
</head>
<body>

<section class="card card--front">
  <div class="brand">
    <span class="brand__dot"></span>
    <span class="brand__name">Bramble Tee Golf</span>
  </div>
  <p class="slogan">Par is Good. Birdie Is Better. Be Better.</p>
  <div class="pitch">
    <p class="pitch__title">Elevator Pitch</p>
    <p class="pitch__line">We work with serious golfers and those that want to be serious golfers…</p>
    <p class="pitch__line">to make you better, faster, at all phases of the game…</p>
    <p class="pitch__line pitch__line--lit">We use the same state-of-the-art technology as professional golfers…</p>
    <p class="pitch__line pitch__line--lit">which produces data sets that shows your improvement in real time.</p>
    <p class="pitch__line pitch__line--lit">Our facility is available 24/7 to our members, which allows you to improve on your time.</p>
  </div>
</section>

<section class="card card--back">
  <div class="identity">
    <div class="person">
      <p class="person__name">DANIEL BROOKS</p>
      <p class="person__role">Director</p>
    </div>
    <span class="divider"></span>
    <ul class="contacts">
      <li>
        <svg viewBox="0 0 12 12" aria-hidden="true"><path d="M2.5 1 L4.5 1 L5.2 3.4 L4 4.3 C4.6 5.8 6.2 7.4 7.7 8 L8.6 6.8 L11 7.5 L11 9.5 C11 10.3 10.3 11 9.5 11 C5 11 1 7 1 2.5 C1 1.7 1.7 1 2.5 1 Z" fill="#d3d3d3"/></svg>
        513-555-0182
      </li>
      <li>
        <svg viewBox="0 0 12 12" aria-hidden="true"><rect x="1" y="2.5" width="10" height="7" fill="none" stroke="#d3d3d3" stroke-width="1.2"/><path d="M1 2.8 L6 6.5 L11 2.8" fill="none" stroke="#d3d3d3" stroke-width="1.2"/></svg>
        info@brambleteegolf.com
      </li>
      <li>
        <svg viewBox="0 0 12 12" aria-hidden="true"><circle cx="6" cy="6" r="4.8" fill="none" stroke="#d3d3d3" stroke-width="1.1"/><ellipse cx="6" cy="6" rx="2" ry="4.8" fill="none" stroke="#d3d3d3" stroke-width="1"/><path d="M1.2 6 H10.8" stroke="#d3d3d3" stroke-width="1"/></svg>
        www.brambleteegolf.com
      </li>
    </ul>
  </div>
  <p class="address"><span class="address__dim">1480 E. Linden RD. Unit B4</span> Fairbrook, OH 45099</p>
</section>

</body>
</html>
```